Stationery & Business Card Design Project

We require our stationary to be professional, which will stand out but also be sophisticated and reputable.

We also require the following:

* Business card must be double sided
* Logo must stand out with brightfund colours used. Other colours may be added but only in small doses as not to overtake the main colours.
* For business card brightfund pty ltd smsf specialists with administrators at bottom left on the front of the card and details on the back

Industry/Entity Type

Business

Requirements
Must have
• * Business Cards
* With compliments slips –2 different ones
* Forwarding mail slip (smaller version of a with compliments slip)

```html
<!DOCTYPE html>
<html lang="en">
<head>
<meta charset="utf-8">
<title>brightfund – stationery</title>
<link rel="stylesheet" href="https://fonts.googleapis.com/css2?family=Open+Sans:wght@400;600;700&family=Pinyon+Script&display=swap">
<style>
  :root {
    --navy: #2e3176;
    --grey: #808285;
    --ink: #1a1a1a;
    --paper: #ffffff;
    --backdrop: #ece8e1;
    --tint: #dcdcec;
    --tint-soft: #eeeef6;
  }
  * { margin: 0; padding: 0; box-sizing: border-box; }
  html, body { width: 1200px; height: 983px; overflow: hidden; }
  body {
    position: relative;
    background: var(--backdrop);
    font-family: "Open Sans", Arial, sans-serif;
    color: var(--ink);
  }
  .piece-label {
    position: absolute;
    font-size: 34px;
    font-weight: 400;
    color: var(--ink);
    white-space: nowrap;
  }
  .piece-label--signature { left: 347px; top: 97px; }
  .piece-label--slip { left: 382px; top: 471px; }

  .sheet {
    position: absolute;
    background: var(--paper);
    box-shadow: 0 2px 6px rgba(0,0,0,0.25);
    overflow: hidden;
  }
  .sheet--signature { left: 21px; top: 179px; width: 1017px; height: 234px; }
  .sheet--slip { left: 31px; top: 537px; width: 1103px; height: 394px; }

  .corner-tint {
    position: absolute;
    top: 0;
    background: linear-gradient(160deg, var(--tint-soft), var(--tint));
  }
  .sheet--signature .corner-tint { right: 0; width: 97px; height: 96px; }
  .sheet--slip .corner-tint { right: 0; width: 191px; height: 206px; }

  .brand { position: absolute; display: flex; align-items: center; gap: 14px; }
  .brand__mark { background: var(--navy); flex: none; }
  .brand__text { display: flex; flex-direction: column; }
  .brand__name {
    font-weight: 600;
    color: var(--navy);
    line-height: 1;
    letter-spacing: -1px;
  }
  .brand__tagline {
    font-size: 13px;
    color: var(--navy);
    letter-spacing: 6px;
    margin-top: 2px;
  }
  .sheet--signature .brand { left: 38px; top: 38px; }
  .sheet--signature .brand__mark { width: 74px; height: 74px; }
  .sheet--signature .brand__name { font-size: 58px; }
  .sheet--slip .brand { left: 34px; top: 34px; }
  .sheet--slip .brand__mark { width: 76px; height: 76px; }
  .sheet--slip .brand__name { font-size: 60px; }

  .person {
    position: absolute;
    left: 139px;
    top: 139px;
    font-size: 32px;
    white-space: nowrap;
  }
  .person__name { font-weight: 700; }
  .person__title { font-weight: 400; }

  .contact { position: absolute; font-size: 18px; white-space: nowrap; }
  .contact__row { display: flex; align-items: center; gap: 8px; height: 29px; }
  .contact__item { display: inline-flex; align-items: center; gap: 7px; margin-right: 10px; }
  .icon { width: 18px; height: 18px; flex: none; }
  .sheet--signature .contact--phones { left: 530px; top: 60px; }
  .sheet--signature .contact--web { left: 530px; top: 152px; }

  .greeting {
    position: absolute;
    left: 28px;
    top: 186px;
    font-family: "Pinyon Script", cursive;
    font-size: 44px;
    color: var(--ink);
  }
  .sheet--slip .contact--lines { left: 28px; top: 314px; }
</style>
</head>
<body>
  <svg width="0" height="0" style="position:absolute">
    <defs>
      <symbol id="ico-phone" viewBox="0 0 20 20"><circle cx="10" cy="10" r="10" fill="#2e3176"/><path d="M6.5 5.5c.6-.6 1.4-.5 1.7.2l.8 1.7c.2.5 0 1-.4 1.3l-.6.4c.6 1.3 1.6 2.3 2.9 2.9l.4-.6c.3-.4.8-.6 1.3-.4l1.7.8c.7.3.8 1.1.2 1.7-1 1-2.6 1.2-4 .4-2-1.1-3.6-2.7-4.6-4.6-.8-1.4-.6-3 .6-3.8z" fill="#fff"/></symbol>
      <symbol id="ico-fax" viewBox="0 0 20 20"><circle cx="10" cy="10" r="10" fill="#2e3176"/><rect x="5" y="8" width="10" height="6" rx="1" fill="#fff"/><rect x="7" y="5" width="6" height="3" fill="#fff"/><rect x="7" y="12" width="6" height="3" fill="#2e3176" stroke="#fff" stroke-width="1"/></symbol>
      <symbol id="ico-mobile" viewBox="0 0 20 20"><circle cx="10" cy="10" r="10" fill="#2e3176"/><rect x="7" y="4.5" width="6" height="11" rx="1.2" fill="#fff"/><rect x="8" y="6" width="4" height="6" fill="#2e3176"/></symbol>
      <symbol id="ico-mail" viewBox="0 0 20 20"><circle cx="10" cy="10" r="10" fill="#2e3176"/><circle cx="10" cy="10" r="4.5" fill="none" stroke="#fff" stroke-width="1.6"/><circle cx="10" cy="10" r="1.6" fill="#fff"/></symbol>
      <symbol id="ico-web" viewBox="0 0 20 20"><circle cx="10" cy="10" r="10" fill="#2e3176"/><circle cx="10" cy="10" r="5.5" fill="none" stroke="#fff" stroke-width="1.2"/><path d="M4.5 10h11M10 4.5c-2.5 3-2.5 8 0 11M10 4.5c2.5 3 2.5 8 0 11" fill="none" stroke="#fff" stroke-width="1"/></symbol>
      <symbol id="ico-home" viewBox="0 0 20 20"><circle cx="10" cy="10" r="10" fill="#2e3176"/><path d="M10 4.5l5.5 5h-1.7v5H11.5v-3h-3v3H6.2v-5H4.5z" fill="#fff"/></symbol>
    </defs>
  </svg>

  <h2 class="piece-label piece-label--signature">e-mail signature</h2>
  <section class="sheet sheet--signature">
    <div class="corner-tint"></div>
    <div class="brand">
      <div class="brand__mark"></div>
      <div class="brand__text">
        <span class="brand__name">brightfund</span>
        <span class="brand__tagline">smsf specialists</span>
      </div>
    </div>
    <p class="person"><span class="person__name">Name</span> | <span class="person__title">Title</span></p>
    <div class="contact contact--phones">
      <div class="contact__row"><svg class="icon"><use href="#ico-phone"/></svg>001-123-123456</div>
      <div class="contact__row"><svg class="icon"><use href="#ico-fax"/></svg>001-123-123456</div>
      <div class="contact__row"><svg class="icon"><use href="#ico-mobile"/></svg>001-123-123456</div>
    </div>
    <div class="contact contact--web">
      <div class="contact__row">
        <span class="contact__item"><svg class="icon"><use href="#ico-mail"/></svg>brightfund@postbox.com</span>
        <span class="contact__item"><svg class="icon"><use href="#ico-web"/></svg>www.Website.com</span>
      </div>
      <div class="contact__row"><svg class="icon"><use href="#ico-home"/></svg>25 Street Name, Road Name, State, Country Code</div>
    </div>
  </section>

  <h2 class="piece-label piece-label--slip">complimentry slip</h2>
  <section class="sheet sheet--slip">
    <div class="corner-tint"></div>
    <div class="brand">
      <div class="brand__mark"></div>
      <div class="brand__text">
        <span class="brand__name">brightfund</span>
        <span class="brand__tagline">smsf specialists</span>
      </div>
    </div>
    <p class="greeting">With Best Compliments</p>
    <div class="contact contact--lines">
      <div class="contact__row">
        <span class="contact__item"><svg class="icon"><use href="#ico-phone"/></svg>001-123-123456</span>
        <span class="contact__item"><svg class="icon"><use href="#ico-fax"/></svg>001-123-123456</span>
        <span class="contact__item"><svg class="icon"><use href="#ico-mobile"/></svg>001-123-123456</span>
      </div>
      <div class="contact__row">
        <span class="contact__item"><svg class="icon"><use href="#ico-mail"/></svg>brightfund@postbox.com</span>
        <span class="contact__item"><svg class="icon"><use href="#ico-web"/></svg>www.Website.com</span>
        <span class="contact__item"><svg class="icon"><use href="#ico-home"/></svg>25 Street Name, Road Name, State, Country Code</span>
      </div>
    </div>
  </section>
</body>
</html>
```